Business Card Design & logo

Residential building renovation and maintenance work.
All carpentry and joinery needs.
Laying solid timber and floating floors.
Kitchen and bathroom makeovers and modifications.
Interior fitouts,
small job specialist. tiling, plastering, painting,

I would like a silver background. With the use of different shades of grey, rustic orange, black and white.
I do not want pictures of hammers, chisels etc. I am looking for a logo to be incorporated into the card.

Industry/Entity Type

Carpentry

Contact Information for Business Card

BTW Renovations and Maintenance
Lionel Pasquet
0471526083
info@btwrefits.com.au
btwrefits.com.au

```html
<!DOCTYPE html>
<html lang="en">
<head>
<meta charset="utf-8">
<title>BTW Renovations and Maintenance – Business Card</title>
<link href="https://fonts.googleapis.com/css2?family=Montserrat:wght@300;400;500;700&display=swap" rel="stylesheet">
<style>
  :root {
    --page-bg: #ffffff;
    --card-light: #e6e6e6;
    --card-edge: #9a9a9a;
    --card-dark: #333333;
    --ink: #111111;
    --on-dark: #ffffff;
    --fan-1: #b9b9b9;
    --fan-2: #a4a4a4;
    --fan-3: #8f8f8f;
    --fan-4: #7a7a7a;
    --fan-5: #636363;
    --fan-6: #4c4c4c;
  }
  html, body {
    margin: 0;
    padding: 0;
    width: 1200px;
    height: 1000px;
    overflow: hidden;
    background: var(--page-bg);
    font-family: "Montserrat", Arial, sans-serif;
  }
  .canvas {
    position: relative;
    width: 1200px;
    height: 1000px;
  }
  .card {
    position: absolute;
    left: 329px;
    width: 542px;
    height: 334px;
    box-sizing: border-box;
    border: 1px solid var(--card-edge);
    background: var(--card-light);
    overflow: hidden;
  }
  .card--front { top: 146px; }
  .card--back { top: 519px; }

  .brand {
    position: absolute;
    left: 0;
    right: 0;
    top: 122px;
    text-align: center;
    color: var(--ink);
  }
  .brand__name {
    display: block;
    font-weight: 700;
    font-size: 62px;
    line-height: 62px;
    letter-spacing: 1px;
    margin-left: 8px;
  }
  .brand__tagline {
    display: block;
    font-weight: 500;
    font-size: 19.5px;
    line-height: 22px;
    margin-top: 4px;
    margin-left: 10px;
  }

  .card__art {
    position: absolute;
    left: 0;
    top: 0;
    width: 540px;
    height: 332px;
  }
  .holder-name {
    position: absolute;
    left: 31px;
    top: 30px;
    margin: 0;
    font-weight: 500;
    font-size: 29px;
    color: var(--ink);
  }
  .contact {
    position: absolute;
    right: 34px;
    top: 68px;
    margin: 0;
    padding: 0;
    list-style: none;
    text-align: right;
    color: var(--on-dark);
  }
  .contact__item {
    display: flex;
    flex-direction: column;
    align-items: flex-end;
    height: 84px;
  }
  .contact__icon {
    width: 24px;
    height: 24px;
    margin-bottom: 4px;
  }
  .contact__text {
    font-weight: 400;
    font-size: 16px;
    letter-spacing: 0.3px;
  }
</style>
</head>
<body>
<main class="canvas">

  <section class="card card--front" aria-label="Card front">
    <div class="brand">
      <span class="brand__name">BTW</span>
      <span class="brand__tagline">Renovations and Maintenance</span>
    </div>
  </section>

  <section class="card card--back" aria-label="Card back">
    <svg class="card__art" viewBox="0 0 540 332" aria-hidden="true">
      <polygon points="331,0 540,0 540,332 138,332" fill="var(--fan-1)"/>
      <polygon points="331,0 540,0 540,332 155,332" fill="var(--fan-2)"/>
      <polygon points="331,0 540,0 540,332 171,332" fill="var(--fan-3)"/>
      <polygon points="331,0 540,0 540,332 187,332" fill="var(--fan-4)"/>
      <polygon points="331,0 540,0 540,332 202,332" fill="var(--fan-5)"/>
      <polygon points="331,0 540,0 540,332 217,332" fill="var(--fan-6)"/>
      <polygon points="331,0 540,0 540,332 219,332" fill="var(--card-dark)"/>
    </svg>

    <h1 class="holder-name">Lionel Pasquet</h1>

    <ul class="contact">
      <li class="contact__item">
        <svg class="contact__icon" viewBox="0 0 24 24" aria-label="Phone">
          <path d="M2 8c0-3 4-5 10-5s10 2 10 5v2h-5V8H7v2H2z" fill="var(--on-dark)"/>
          <path d="M7 10l2-2h6l2 2 3 9H4z" fill="var(--on-dark)"/>
          <g fill="var(--card-dark)">
            <rect x="9" y="12" width="1.6" height="1.6"/><rect x="11.2" y="12" width="1.6" height="1.6"/><rect x="13.4" y="12" width="1.6" height="1.6"/>
            <rect x="9" y="14.4" width="1.6" height="1.6"/><rect x="11.2" y="14.4" width="1.6" height="1.6"/><rect x="13.4" y="14.4" width="1.6" height="1.6"/>
          </g>
        </svg>
        <span class="contact__text">0471526083</span>
      </li>
      <li class="contact__item">
        <svg class="contact__icon" viewBox="0 0 24 24" aria-label="Email">
          <rect x="1" y="5" width="22" height="15" fill="var(--on-dark)"/>
          <path d="M1.5 5.5L12 14 22.5 5.5" fill="none" stroke="var(--card-dark)" stroke-width="1.4"/>
        </svg>
        <span class="contact__text">info@btwrefits.com.au</span>
      </li>
      <li class="contact__item">
        <svg class="contact__icon" viewBox="0 0 24 24" aria-label="Website">
          <circle cx="12" cy="12" r="10.5" fill="var(--on-dark)"/>
          <rect x="0" y="9.5" width="24" height="5" fill="var(--card-dark)"/>
          <text x="12" y="13.6" text-anchor="middle" font-family="Montserrat, Arial, sans-serif" font-size="5" font-weight="700" fill="var(--on-dark)">www</text>
        </svg>
        <span class="contact__text">btwrefits.com.au</span>
      </li>
    </ul>
  </section>

</main>
</body>
</html>
```